Home Security Company Business Card

Looking for a eye catching business card that is non traditional and stands out but yet still looks professional. It should include all the pertinent information such as name, title, address, telephone, e-mail, website address should definitely stand out and then finally the logo.

Target Market(s)

Residential and Commercial accounts mostly upscale accounts

Industry/Entity Type

Security

Contact Information for Business Card

Name
Title
Address
Office #
Cell #
E-mail
Website

Font styles to use
Serif
Sans Serif

Requirements
Must have
• Logo, two sided color configuration
Nice to have
• You decide
Should not have
• There really aren't any.

```html
<!DOCTYPE html>
<html lang="en">
<head>
<meta charset="utf-8">
<title>Harborline Protection Group – Business Card</title>
<link rel="stylesheet" href="https://fonts.googleapis.com/css2?family=Josefin+Sans:wght@400;600&family=Questrial&display=swap">
<style>
  :root {
    --backdrop: #d6d6d6;
    --card-white: #f3f2f0;
    --brand-red: #721214;
    --brand-gold: #d9a431;
    --text-grey: #7a7a7a;
    --text-light: #f4ecec;
  }
  * { box-sizing: border-box; margin: 0; padding: 0; }
  html, body {
    width: 1200px; height: 900px; overflow: hidden;
    background: var(--backdrop);
  }
  .canvas { position: relative; width: 1200px; height: 900px; }
  .card {
    position: absolute; width: 490px; height: 280px;
    background: var(--card-white);
    box-shadow: 0 2px 6px rgba(0,0,0,0.12);
    overflow: hidden;
  }
  .card--front { left: 220px; top: 170px; display: flex; align-items: center; justify-content: center; }
  .card--back { left: 490px; top: 450px; display: flex; }

  .brand { display: flex; align-items: center; gap: 14px; }
  .brand__dot { width: 18px; height: 18px; border-radius: 50%; background: var(--brand-red); }
  .brand__name {
    font-family: 'Josefin Sans', sans-serif; font-weight: 600;
    font-size: 26px; letter-spacing: 1px; text-transform: uppercase;
    color: var(--brand-red); line-height: 1.1;
  }

  .identity {
    width: 282px; background: var(--brand-red);
    display: flex; flex-direction: column; justify-content: center;
    padding-left: 42px;
  }
  .identity__name {
    font-family: 'Josefin Sans', sans-serif; font-weight: 400;
    font-size: 27px; letter-spacing: 1.5px; color: var(--text-light);
    text-transform: uppercase;
  }
  .identity__title {
    font-family: 'Josefin Sans', sans-serif; font-size: 11px;
    letter-spacing: 1.5px; color: var(--text-light); opacity: .85;
    text-transform: uppercase; margin-top: 4px; padding-left: 10px;
  }
  .gold-band { width: 16px; background: var(--brand-gold); }

  .contacts {
    flex: 1; display: flex; flex-direction: column; justify-content: center;
    gap: 12px; padding-left: 18px;
  }
  .contact { display: flex; align-items: flex-start; gap: 12px; }
  .contact__icon { flex: none; width: 18px; height: 18px; }
  .contact__text {
    font-family: 'Questrial', sans-serif; font-size: 11.5px;
    line-height: 1.35; color: var(--text-grey);
  }
</style>
</head>
<body>
<main class="canvas">
  <section class="card card--front" aria-label="Card front">
    <div class="brand">
      <span class="brand__dot"></span>
      <span class="brand__name">Harborline<br>Protection Group</span>
    </div>
  </section>

  <section class="card card--back" aria-label="Card back">
    <div class="identity">
      <h1 class="identity__name">Daniel Reyes</h1>
      <p class="identity__title">General Manager</p>
    </div>
    <div class="gold-band"></div>
    <div class="contacts">
      <div class="contact">
        <svg class="contact__icon" viewBox="0 0 18 18" aria-hidden="true">
          <circle cx="9" cy="9" r="9" fill="var(--brand-red)"/>
          <path d="M6 5.2c.5-.4 1-.3 1.3.2l.7 1.2c.2.4.1.8-.2 1.1l-.4.3c.4.9 1.1 1.6 2 2l.3-.4c.3-.3.7-.4 1.1-.2l1.2.7c.5.3.6.8.2 1.3-.6.8-1.5 1-2.4.6-1.8-.8-3.1-2.1-3.9-3.9-.4-.9-.2-1.8.1-2.9z" fill="#fff"/>
        </svg>
        <p class="contact__text">Cell: 123 456 789<br>Office: 123 456 789</p>
      </div>
      <div class="contact">
        <svg class="contact__icon" viewBox="0 0 18 18" aria-hidden="true">
          <circle cx="9" cy="9" r="9" fill="var(--brand-red)"/>
          <circle cx="9" cy="9" r="4.2" fill="none" stroke="#fff" stroke-width="1"/>
          <path d="M4.8 9h8.4M9 4.8c-1.6 2.6-1.6 5.8 0 8.4M9 4.8c1.6 2.6 1.6 5.8 0 8.4" fill="none" stroke="#fff" stroke-width="1"/>
        </svg>
        <p class="contact__text">dreyes@harborline.com<br>harborline.com</p>
      </div>
      <div class="contact">
        <svg class="contact__icon" viewBox="0 0 18 18" aria-hidden="true">
          <circle cx="9" cy="9" r="9" fill="var(--brand-red)"/>
          <path d="M9 4.2a3.3 3.3 0 0 0-3.3 3.3c0 2.4 3.3 6 3.3 6s3.3-3.6 3.3-6A3.3 3.3 0 0 0 9 4.2z" fill="#fff"/>
          <circle cx="9" cy="7.5" r="1.2" fill="var(--brand-red)"/>
        </svg>
        <p class="contact__text">Address Line 1<br>Address Line 2</p>
      </div>
    </div>
  </section>
</main>
</body>
</html>
```